Homepage design change needed

We're looking for a designer to change the way our homepage looks according to the attached sketch along with the project brief below.
Existing website is: http://www.tallowpine.co.nz
Please download the sketched design from the link below. https://www.filecrate.example/s/k3mq7rt2wz9pla4/homepagesketches2.zip
There are 4 images inside the above zip file. front1, 2 & 3 make up the homepage.
page2.jpg is a sketch of what we'd like instead of the current page http://www.tallowpine.co.nz/join-tallowpine.aspx
Requirements
Must have
- The design must keep the following elements the same as the existing website:
- colour scheme
- same width
- same rounded corners/soft edges
- rounded buttons
- the graphics look of the following video brought through into the illustrations http://www.tallowpine.co.nz/help/video.aspx
front1.jpg - there is an illustration (3 boxes with = success! written); please don't design an illustration, simply leave space for a graphic to be put in its place later.
front2 and 3.jpg are to be fully designed as sketched. (again please ignore the illustration with 3 boxes = success!)

```html
<!DOCTYPE html>
<html lang="en">
<head>
<meta charset="utf-8">
<title>Tallow Pine – Create your profile</title>
<link rel="stylesheet" href="https://fonts.googleapis.com/css2?family=Raleway:wght@400;500;600;700&display=swap">
<style>
  :root {
    --page-bg: #ebebeb;
    --card-bg: #ffffff;
    --brand: #0c8ef8;
    --brand-dark: #0660b0;
    --placeholder: #9a9a9a;
    --white: #ffffff;
  }
  * { box-sizing: border-box; margin: 0; padding: 0; }
  html, body {
    width: 1200px; height: 1091px; overflow: hidden;
    background: var(--page-bg);
    font-family: "Raleway", Arial, sans-serif;
    color: var(--brand);
  }
  .page { position: relative; width: 1200px; height: 1091px; }

  .card {
    position: absolute; left: 76px; top: 33px; width: 1047px; height: 974px;
    background: var(--card-bg);
    border: 1px solid var(--brand);
    border-radius: 4px;
  }
  .site-header {
    position: absolute; left: 76px; top: 34px; width: 1047px; height: 117px;
    display: flex; align-items: center; justify-content: center;
    padding-bottom: 8px;
  }
  .wordmark {
    display: flex; align-items: center; gap: 10px;
    font-size: 38px; font-weight: 600; color: var(--brand); letter-spacing: 0.5px;
  }
  .wordmark-dot {
    width: 14px; height: 14px; border-radius: 50%; background: var(--brand);
  }
  .header-shadow {
    position: absolute; left: 76px; top: 138px; width: 1047px; height: 13px;
    background: linear-gradient(to bottom, rgba(0,0,0,0) 0%, rgba(0,0,0,0.18) 100%);
  }
  .ribbon-fold { position: absolute; top: 129px; }
  .ribbon-fold.left { left: 55px; }
  .ribbon-fold.right { left: 1123px; }

  .tagline-banner {
    position: absolute; left: 55px; top: 151px; width: 1091px; height: 132px;
    background: var(--brand);
    color: var(--white);
    display: flex; align-items: center; justify-content: center;
    text-align: center;
    font-size: 26px; line-height: 40px; font-weight: 400;
  }

  .section-title {
    position: absolute; left: 118px; top: 327px;
    font-size: 24px; font-weight: 400;
  }
  .section-subtitle {
    position: absolute; left: 118px; top: 408px;
    font-size: 21px; font-weight: 600;
  }

  .profile-row { position: absolute; left: 120px; width: 540px; height: 90px; }
  .profile-row.r1 { top: 496px; }
  .profile-row.r2 { top: 649px; }
  .profile-row.r3 { top: 802px; }
  .profile-audience {
    position: absolute; left: 0; top: 0; width: 130px;
    list-style: none; font-size: 16.5px; line-height: 33px; font-weight: 500;
  }
  .profile-row.r1 .profile-audience { top: -6px; }
  .profile-row.r2 .profile-audience { top: 8px; }
  .profile-row.r3 .profile-audience { top: -4px; font-size: 15px; }
  .profile-photo {
    position: absolute; left: 142px; top: 0; width: 87px; height: 87px;
    background: var(--placeholder); border-radius: 4px;
  }
  .profile-info { position: absolute; left: 251px; top: -10px; }
  .profile-name { font-size: 19.5px; font-weight: 400; line-height: 28px; }
  .profile-role {
    font-size: 12px; font-weight: 700; letter-spacing: 1.3px;
    text-transform: uppercase; margin-top: 3px; margin-bottom: 12px;
  }
  .profile-blurb { font-size: 12.5px; line-height: 20px; font-weight: 500; }

  .join-panel {
    position: absolute; left: 764px; top: 384px; width: 284px; height: 576px;
    background: var(--brand); border-radius: 4px; color: var(--white);
    padding: 24px 22px 0 21px;
  }
  .join-title { font-size: 19.5px; font-weight: 600; margin-bottom: 55px; }
  .field { display: block; margin-bottom: 21px; }
  .field-label { display: block; font-size: 16.5px; font-weight: 500; line-height: 20px; margin-bottom: 5px; }
  .field-input {
    display: block; width: 240px; height: 36px;
    background: var(--white); border: 1px solid #d8e8f7; border-radius: 3px;
    font-family: inherit;
  }
  .next-button {
    position: absolute; right: 22px; bottom: 28px;
    width: 86px; height: 43px;
    background: transparent; color: var(--white);
    border: 2px solid var(--white); border-radius: 2px;
    font-family: inherit; font-size: 19px; font-weight: 500;
  }
</style>
</head>
<body>
<div class="page">
  <div class="card"></div>

  <header class="site-header">
    <div class="wordmark"><span>tallowpine.co.nz</span><span class="wordmark-dot"></span></div>
  </header>
  <div class="header-shadow"></div>

  <svg class="ribbon-fold left" width="21" height="22" viewBox="0 0 21 22"><polygon points="21,0 21,22 0,22" fill="#0660b0"/></svg>
  <svg class="ribbon-fold right" width="23" height="22" viewBox="0 0 23 22"><polygon points="0,0 23,22 0,22" fill="#0660b0"/></svg>

  <section class="tagline-banner">
    <p>The place to hire and be hired putting you<br>in the driver seat (where you belong).</p>
  </section>

  <h1 class="section-title">Create your profile now</h1>
  <h2 class="section-subtitle">We have&nbsp; a profile to suit you</h2>

  <div class="profile-row r1">
    <ul class="profile-audience"><li>Job Seekers</li><li>Contractors</li><li>Freelancers</li></ul>
    <div class="profile-photo" role="img" aria-label="Profile photo of a dancer"></div>
    <div class="profile-info">
      <h3 class="profile-name">Hazel Marsh</h3>
      <p class="profile-role">Dancer</p>
      <p class="profile-blurb">Lorem ipsum dolor<br>Lorem ipsum color</p>
    </div>
  </div>

  <div class="profile-row r2">
    <ul class="profile-audience"><li>Small Business</li><li>Self Employed</li></ul>
    <div class="profile-photo" role="img" aria-label="Profile photo of a local builder"></div>
    <div class="profile-info">
      <h3 class="profile-name">Local Builder</h3>
      <p class="profile-role">Something</p>
      <p class="profile-blurb">Lorem ipsum dolor<br>Lorem ipsum color</p>
    </div>
  </div>

  <div class="profile-row r3">
    <ul class="profile-audience"><li>Currently working</li><li>or maintaining</li><li>privacy</li></ul>
    <div class="profile-photo" role="img" aria-label="Profile photo of a sales person"></div>
    <div class="profile-info">
      <h3 class="profile-name">Sales person of the year</h3>
      <p class="profile-role">Sales</p>
      <p class="profile-blurb">Lorem ipsum dolor<br>Lorem ipsum color</p>
    </div>
  </div>

  <form class="join-panel">
    <h2 class="join-title">Join now (it’s free)</h2>
    <label class="field"><span class="field-label">First name</span><input class="field-input" type="text"></label>
    <label class="field"><span class="field-label">Last name</span><input class="field-input" type="text"></label>
    <label class="field"><span class="field-label">Email address</span><input class="field-input" type="email"></label>
    <label class="field"><span class="field-label">Tallow Pine name</span><input class="field-input" type="text"></label>
    <label class="field"><span class="field-label">Password</span><input class="field-input" type="password"></label>
    <button class="next-button" type="button">Next</button>
  </form>
</div>
</body>
</html>
```